Event flyer for Sunday night Youth Group

Need a 4 x 6 or 5 x 7 flyer for a new youth group starting on April 14. The youth group is for students in middle school and high school so it needs to look fun and cool, but not childish. I prefer it not to include pictures of people unless it's so obscure you can't really see their faces. I've uploaded some pictures of flyers I like. I've also attached a couple versions of our logo to use on the flyer.
Information the flyer needs to include:
Youth Group
Sundays, 6-8pm (beginning April 14)
Location: Merriwick's - 4219 Hollowfern Ln S, Ashbury, 97418
There will be dinner, games, friends, and a message.
Target Market(s)
Youth ages 13-18
Industry/Entity Type
Church
Colors
Designer to choose colors to be used in the design.
Look and feel

```html
<!DOCTYPE html>
<html lang="en">
<head>
<meta charset="utf-8">
<title>Youth Group – Sunday Nights</title>
<link rel="stylesheet" href="https://fonts.googleapis.com/css2?family=Montserrat:wght@500;600;700;800&family=Oswald:wght@500;600;700&family=Pacifico&display=swap">
<style>
  :root {
    --sage: #86968c;
    --sage-dark: #5f6f68;
    --navy: #1f2a44;
    --orange: #f58a3a;
    --amber: #f8b63a;
    --coral: #ef5a6b;
    --magenta: #b2358f;
    --violet: #6b3fa0;
    --sky: #3fa7d6;
    --white: #ffffff;
  }
  * { margin: 0; padding: 0; box-sizing: border-box; }
  html, body { width: 857px; height: 1200px; overflow: hidden; background: var(--sage); }
  .flyer {
    position: relative;
    width: 857px;
    height: 1200px;
    overflow: hidden;
    font-family: "Montserrat", sans-serif;
    color: var(--white);
  }
  .flyer__backdrop {
    position: absolute;
    inset: 0;
    background:
      radial-gradient(circle at 12% 18%, rgba(63,167,214,0.35), transparent 30%),
      radial-gradient(circle at 88% 30%, rgba(245,138,58,0.35), transparent 32%),
      radial-gradient(circle at 15% 80%, rgba(245,138,58,0.30), transparent 30%),
      radial-gradient(circle at 85% 85%, rgba(63,167,214,0.30), transparent 30%),
      linear-gradient(160deg, #8c9b91 0%, var(--sage) 50%, var(--sage-dark) 100%);
  }
  .brand {
    position: absolute;
    top: 88px;
    left: 0;
    width: 100%;
    display: flex;
    flex-direction: column;
    align-items: center;
    gap: 22px;
  }
  .brand__mark {
    width: 64px;
    height: 64px;
    background: var(--white);
  }
  .brand__name {
    font-weight: 700;
    font-size: 26px;
    letter-spacing: 2px;
    color: var(--white);
    line-height: 1;
  }
  .badge {
    position: absolute;
    left: 168px;
    top: 270px;
    width: 520px;
    height: 520px;
  }
  .badge svg { position: absolute; inset: 0; }
  .badge__text {
    position: absolute;
    inset: 0;
    display: flex;
    flex-direction: column;
    align-items: center;
    padding-top: 150px;
  }
  .badge__title {
    font-family: "Pacifico", cursive;
    font-size: 104px;
    line-height: 1;
    color: var(--white);
    text-shadow: 4px 4px 0 var(--magenta);
  }
  .badge__subtitle {
    margin-top: -6px;
    font-family: "Oswald", sans-serif;
    font-weight: 600;
    font-size: 58px;
    line-height: 1.1;
    letter-spacing: 1px;
    color: var(--white);
  }
  .badge__when {
    margin-top: 32px;
    font-family: "Oswald", sans-serif;
    font-weight: 600;
    font-size: 50px;
    line-height: 1.1;
    color: var(--amber);
  }
  .badge__start {
    margin-top: 4px;
    font-weight: 700;
    font-size: 22px;
    color: var(--white);
  }
  .venue {
    position: absolute;
    left: 100px;
    top: 956px;
    width: 657px;
    height: 50px;
    background: linear-gradient(90deg, var(--sky), #9ccbe0 45%, #f09ab7 75%, var(--coral));
    display: flex;
    align-items: center;
    justify-content: center;
    font-family: "Oswald", sans-serif;
    font-weight: 600;
    font-size: 27px;
    color: var(--navy);
    letter-spacing: 0.3px;
  }
  .agenda {
    position: absolute;
    left: 0;
    top: 1046px;
    width: 100%;
    display: flex;
    flex-direction: column;
    align-items: center;
  }
  .agenda__lead {
    display: flex;
    align-items: center;
    gap: 12px;
    font-weight: 700;
    font-size: 11px;
    letter-spacing: 2px;
  }
  .agenda__lead::before, .agenda__lead::after {
    content: "";
    width: 60px;
    height: 2px;
    background: var(--white);
  }
  .agenda__list {
    margin-top: 8px;
    width: 657px;
    height: 50px;
    background: var(--navy);
    display: flex;
    align-items: center;
    justify-content: center;
    font-weight: 600;
    font-size: 28px;
    color: var(--white);
  }
</style>
</head>
<body>
  <main class="flyer">
    <div class="flyer__backdrop" role="img" aria-label="Flowing swirl pattern of sage, orange and blue contour lines"></div>

    <header class="brand">
      <span class="brand__mark"></span>
      <span class="brand__name">WAYPOINT FELLOWSHIP</span>
    </header>

    <section class="badge">
      <svg viewBox="0 0 520 520" aria-hidden="true">
        <defs>
          <linearGradient id="badgeFill" x1="0" y1="0" x2="0" y2="1">
            <stop offset="0" stop-color="#f7a33a"/>
            <stop offset="0.45" stop-color="#ef5a6b"/>
            <stop offset="0.8" stop-color="#b2358f"/>
            <stop offset="1" stop-color="#6b3fa0"/>
          </linearGradient>
        </defs>
        <circle cx="260" cy="260" r="258" fill="#3fa7d6"/>
        <circle cx="260" cy="260" r="246" fill="url(#badgeFill)"/>
        <circle cx="260" cy="260" r="222" fill="none" stroke="#ffffff" stroke-opacity="0.25" stroke-width="2"/>
        <circle cx="260" cy="260" r="196" fill="none" stroke="#ffffff" stroke-opacity="0.2" stroke-width="2"/>
        <circle cx="260" cy="260" r="170" fill="none" stroke="#ffffff" stroke-opacity="0.15" stroke-width="2"/>
      </svg>
      <div class="badge__text">
        <h1 class="badge__title">youth</h1>
        <p class="badge__subtitle">GROUP</p>
        <p class="badge__when">SUNDAYS, 6-8PM</p>
        <p class="badge__start">beginning April 14</p>
      </div>
    </section>

    <p class="venue">MERRIWICK'S - 4219 HOLLOWFERN LN S, ASHBURY, 97418</p>

    <section class="agenda">
      <p class="agenda__lead">THERE WILL BE</p>
      <p class="agenda__list">dinner, games, friends, and a message</p>
    </section>
  </main>
</body>
</html>
```